I need a flyer made , the flyer can be one page or two pages or three pages . I will be posting this on Instagram and social media platforms. I am a luxury home builder , I am looking to hire a construction project manager . Below are some examples and ideas what can be on the flyer

We’re looking for a construction project manager who’s passionate about building luxury homes at the highest standards
We’re hiring construction project manager
* Experience 5+ years in residential project management with a strong portfolio of completed homes.
* location : Bergen County NJ
* excellent leadership skills, leads teams with confidence and clarity
* communicates seamlessly with architects , engineers, designers and clients
*knows how to manage budgets and timelines without compromising quality
*solves problems with a positive solution first mindset
* pays attention to every detail because in luxury the small things are the big things

Apply now , link in bio or DM to connect.

My logo is attached, my web site www.pinecrestbuildworks.com
My style is modern but still warm and inviting. I like a clean classy look .
Updates

Please don’t add any images of chairs or people to the flyer , I do not want people on my flyer. Do not add standard images of offices and houses , we are luxury builders , we build homes over 2 million dollars. Keep a classy , simple modern look . High end .

You can add a white hard hat with my logo on it for a image , this is a suggestion does not have to be on my flyer ,

```html
<!DOCTYPE html>
<html lang="en">
<head>
<meta charset="utf-8">
<title>Pinecrest Buildworks – Hiring Construction Project Manager</title>
<link rel="stylesheet" href="https://fonts.googleapis.com/css2?family=Poppins:wght@400;600;700&family=Roboto+Condensed:wght@700&family=Russo+One&display=swap">
<style>
  :root {
    --ink: #000000;
    --paper: #ffffff;
    --ring: #8a8a8a;
    --disc: #9b9b9b;
    --placeholder-light: #f4f4f4;
    --placeholder-dark: #dcdcdc;
  }
  * { box-sizing: border-box; margin: 0; padding: 0; }
  html, body { width: 1200px; height: 1200px; overflow: hidden; background: var(--ink); }
  .flyer { position: relative; width: 1200px; height: 1200px; background: var(--ink); color: var(--paper); overflow: hidden; font-family: "Poppins", sans-serif; }
  .shapes { position: absolute; inset: 0; }
  .headline { position: absolute; left: 0; top: 0; width: 1200px; height: 400px; }
  .role-title {
    position: absolute; left: 67px; top: 434px; width: 569px; height: 114px;
    border: 3px solid var(--paper); border-radius: 14px;
    display: flex; align-items: center; padding-left: 15px;
    font-family: "Roboto Condensed", sans-serif; font-weight: 700; font-size: 40px;
  }
  .requirements-title {
    position: absolute; left: 80px; top: 590px;
    font-family: "Russo One", sans-serif; font-size: 36px; letter-spacing: 0.5px;
  }
  .requirements { position: absolute; left: 78px; top: 648px; width: 570px; list-style: none; }
  .requirements li {
    position: relative; padding-left: 36px; font-size: 18.5px; line-height: 28px;
    margin-bottom: 9px;
  }
  .requirements li svg { position: absolute; left: 2px; top: 8px; width: 15px; height: 15px; }
  .apply-button {
    position: absolute; left: 78px; top: 1092px; width: 186px; height: 61px;
    background: var(--paper); color: var(--ink);
    display: flex; align-items: center; justify-content: center;
    font-weight: 700; font-size: 22px;
  }
  .sign {
    position: absolute; left: 722px; top: 698px; width: 317px; height: 224px;
    background: var(--paper); color: var(--ink); border: 3px solid #3a3a3a;
    display: flex; align-items: center; justify-content: center; text-align: center;
    font-weight: 700; font-size: 58px; line-height: 62px;
  }
  .brand {
    position: absolute; left: 748px; top: 1040px; width: 340px; text-align: center;
    font-size: 31px; font-weight: 400; letter-spacing: 1px;
  }
  .website {
    position: absolute; left: 748px; top: 1127px; width: 340px; text-align: center;
    font-size: 20px; font-weight: 400;
  }
</style>
</head>
<body>
<main class="flyer">
  <svg class="shapes" width="1200" height="1200" viewBox="0 0 1200 1200" aria-hidden="true">
    <defs>
      <linearGradient id="illustrationTone" x1="0" y1="0" x2="1" y2="1">
        <stop offset="0" stop-color="var(--placeholder-light)"/>
        <stop offset="1" stop-color="var(--placeholder-dark)"/>
      </linearGradient>
    </defs>
    <circle class="ring" cx="1156" cy="70" r="16" fill="none" stroke="var(--ring)" stroke-width="4"/>
    <circle class="ring" cx="698" cy="669" r="16" fill="none" stroke="var(--ring)" stroke-width="4"/>
    <circle class="ring" cx="36" cy="1164" r="16" fill="none" stroke="var(--ring)" stroke-width="4"/>
    <circle class="corner-disc" cx="1208" cy="1078" r="96" fill="var(--disc)"/>
    <circle class="spotlight" cx="972" cy="711" r="222" fill="var(--paper)"/>
  </svg>

  <svg class="headline" width="1200" height="400" viewBox="0 0 1200 400" role="img" aria-label="We are hiring!">
    <path class="bubble-frame" d="M717 39 H833 A34 34 0 0 1 867 73 V327 A34 34 0 0 1 833 361 H680 M444 361 H106 A34 34 0 0 1 72 327 V73 A34 34 0 0 1 106 39 H634" fill="none" stroke="var(--paper)" stroke-width="5"/>
    <rect class="bubble" x="102" y="69" width="739" height="261" rx="28" fill="var(--paper)"/>
    <path class="bubble-tail" d="M548 328 L600 386 L652 328 Z" fill="var(--paper)"/>
    <text x="198" y="153" font-family="Russo One, sans-serif" font-size="46" fill="var(--ink)" textLength="192" lengthAdjust="spacingAndGlyphs">WE ARE</text>
    <text x="194" y="273" font-family="Russo One, sans-serif" font-size="142" fill="var(--ink)" textLength="552" lengthAdjust="spacingAndGlyphs">HIRING!</text>
  </svg>

  <div class="role-title">Construction Project Manager</div>

  <h2 class="requirements-title">Requirement :</h2>
  <ul class="requirements">
    <li><svg viewBox="0 0 16 16"><circle cx="8" cy="8" r="6.5" fill="none" stroke="#fff" stroke-width="1.5"/><path d="M4.5 8.2 L7.2 10.8 L14.5 3" fill="none" stroke="#fff" stroke-width="1.8"/></svg>Experience 5+ Years In Residential Project Management With A Strong Portfolio Of Completed Homes.</li>
    <li><svg viewBox="0 0 16 16"><circle cx="8" cy="8" r="6.5" fill="none" stroke="#fff" stroke-width="1.5"/><path d="M4.5 8.2 L7.2 10.8 L14.5 3" fill="none" stroke="#fff" stroke-width="1.8"/></svg>Location : Bergen County NJ</li>
    <li><svg viewBox="0 0 16 16"><circle cx="8" cy="8" r="6.5" fill="none" stroke="#fff" stroke-width="1.5"/><path d="M4.5 8.2 L7.2 10.8 L14.5 3" fill="none" stroke="#fff" stroke-width="1.8"/></svg>Excellent Leadership Skills, Leads Teams With Confidence And Clarity</li>
    <li><svg viewBox="0 0 16 16"><circle cx="8" cy="8" r="6.5" fill="none" stroke="#fff" stroke-width="1.5"/><path d="M4.5 8.2 L7.2 10.8 L14.5 3" fill="none" stroke="#fff" stroke-width="1.8"/></svg>Communicates Seamlessly With Architects , Engineers, Designers And Clients</li>
    <li><svg viewBox="0 0 16 16"><circle cx="8" cy="8" r="6.5" fill="none" stroke="#fff" stroke-width="1.5"/><path d="M4.5 8.2 L7.2 10.8 L14.5 3" fill="none" stroke="#fff" stroke-width="1.8"/></svg>Knows How To Manage Budgets And Timelines Without Compromising Quality</li>
    <li><svg viewBox="0 0 16 16"><circle cx="8" cy="8" r="6.5" fill="none" stroke="#fff" stroke-width="1.5"/><path d="M4.5 8.2 L7.2 10.8 L14.5 3" fill="none" stroke="#fff" stroke-width="1.8"/></svg>Solves Problems With A Positive Solution First Mindset</li>
    <li><svg viewBox="0 0 16 16"><circle cx="8" cy="8" r="6.5" fill="none" stroke="#fff" stroke-width="1.5"/><path d="M4.5 8.2 L7.2 10.8 L14.5 3" fill="none" stroke="#fff" stroke-width="1.8"/></svg>Pays Attention To Every Detail Because In Luxury The Small Things Are The Big Things</li>
  </ul>

  <div class="apply-button">APPLY NOW</div>

  <svg class="shapes" width="1200" height="1200" viewBox="0 0 1200 1200">
    <rect class="illustration-area" role="img" aria-label="Illustration of a hand in a white sleeve reaching in from the right to hold up the sign"
      x="862" y="480" width="338" height="230" fill="url(#illustrationTone)"/>
  </svg>

  <div class="sign">JOIN OUR<br>TEAM</div>

  <div class="brand">Pinecrest Buildworks</div>
  <div class="website">www.pinecrestbuildworks.com</div>
</main>
</body>
</html>
```